BRIGHT CORAL INC , CELL PHONE STORE

We need website design . we already have one but not happy with it www.brightcoralinc.example
we cell phones provide service ,phone repair ,
phone accessories.
online sale payment via PayVerra
shipping by NPDX

Industry/Entity Type

Cell Phone

Number of Pages Required

5+ page

Font styles to use
Serif
Sans Serif

Colors
3176b5

Requirements
Must have
• online sale via PayVerra
Nice to have
• email address

```html
<!DOCTYPE html>
<html lang="en">
<head>
<meta charset="utf-8">
<title>Bright Coral Inc — Cell Phone Store</title>
<link rel="stylesheet" href="https://fonts.googleapis.com/css2?family=Open+Sans:wght@400;600;700&display=swap">
<style>
:root{
  --red:#e84c3d;
  --blue:#3176b5;
  --ink:#2b2b2b;
  --muted:#8a8a8a;
  --line:#dcdcdc;
  --soft:#f5f7fa;
  --white:#ffffff;
  --hero-a:#1c1d22;
  --hero-b:#3a3128;
}
*{box-sizing:border-box;margin:0;padding:0}
html,body{width:1200px;height:2585px;overflow:hidden}
body{font-family:"Open Sans",Arial,sans-serif;color:var(--ink);background:var(--white);position:relative}
.abs{position:absolute}
svg{display:block}

/* top bar */
.topbar{position:absolute;left:0;top:0;width:1200px;height:33px;background:#f3f3f3;border-bottom:1px solid #e6e6e6;font-size:13px;color:#888}
.topbar .item{position:absolute;top:0;height:33px;display:flex;align-items:center;gap:7px;padding:0 10px;border-right:1px solid #e0e0e0}
.social-dot{width:12px;height:12px;border-radius:50%;background:#9a9a9a}

/* nav */
.navbar{position:absolute;left:0;top:33px;width:1200px;height:70px;background:var(--white);border-bottom:1px solid #eee}
.brand{position:absolute;left:110px;top:20px;font-size:27px;font-weight:600;color:var(--red);letter-spacing:.5px}
.nav-links{position:absolute;left:443px;top:0;height:70px;display:flex}
.nav-links a{display:flex;align-items:center;height:70px;padding:0 12px;font-size:13px;color:#666;text-decoration:none;border-left:1px solid #eee}
.nav-links a.active{border-top:3px solid var(--blue)}

/* hero */
.hero{position:absolute;left:0;top:103px;width:1200px;height:605px;background:radial-gradient(circle at 20% 30%,#5b4632 0,transparent 30%),radial-gradient(circle at 60% 15%,#4a3a2c 0,transparent 25%),linear-gradient(180deg,var(--hero-a),var(--hero-b) 85%,#4a3526)}
.hero-phones{position:absolute;left:648px;top:60px;width:560px;height:545px;background:linear-gradient(160deg,#e9eaee,#6f7ea8 40%,#2c3248);border-radius:30px 30px 0 0;opacity:.9}
.hero-copy{position:absolute;left:114px;top:170px;color:var(--white)}
.hero-copy .lead{font-size:26px}
.hero-copy h1{font-size:40px;font-weight:700;color:var(--blue);margin-top:4px}
.hero-copy .sub{font-size:28px;margin-top:8px}
.hero-copy p{font-size:15px;line-height:22px;width:430px;margin-top:16px}
.btn-red{display:inline-flex;align-items:center;gap:8px;background:var(--red);color:var(--white);font-size:14px;font-weight:600;padding:0 22px;height:44px;margin-top:30px;text-transform:uppercase}

/* sections */
.section-title{position:absolute;left:0;width:1200px;text-align:center;font-size:31px;font-weight:700}
.section-title span{color:var(--red);font-weight:400}
.service{position:absolute;top:828px;width:300px}
.service h3{font-size:22px;font-weight:600;margin-top:14px}
.service p{font-size:14px;line-height:31px;color:var(--muted);margin-top:14px}

.tabs{position:absolute;left:420px;top:1093px;width:359px;height:49px;border:1px solid #e4e4e4;display:flex}
.tabs div{flex:1;display:flex;align-items:center;justify-content:center;font-size:14px;color:#999;border-right:1px solid #e4e4e4;font-weight:600}
.tabs div.on{color:var(--blue);border-right:0}

.product{position:absolute;top:1186px;width:225px;height:387px;border:1px solid #ececec;background:var(--white)}
.product.lift{box-shadow:0 4px 14px rgba(0,0,0,.12)}
.product .shot{position:absolute;left:55px;top:24px;width:115px;height:240px;border-radius:16px;background:linear-gradient(160deg,#3a3a3a,#0f0f0f)}
.product .name{position:absolute;left:17px;top:288px;font-size:20px}
.product .price{position:absolute;right:17px;top:288px;font-size:20px;font-weight:700}
.product .buy{position:absolute;left:52px;top:330px;width:100px;height:36px;border:1px solid #aaa;display:flex;align-items:center;justify-content:center;font-size:16px;color:#555}
.product .buy.on{background:var(--red);border-color:var(--red);color:var(--white)}
.tools{position:absolute;right:16px;top:24px;display:flex;flex-direction:column;gap:8px}
.tools div{width:32px;height:32px;border:1px solid #777;border-radius:4px;display:flex;align-items:center;justify-content:center}

.delivery{position:absolute;left:0;top:1630px;width:1200px;height:90px;background:var(--red);color:var(--white)}
.delivery .label{position:absolute;left:261px;top:32px;font-size:20px;font-weight:600}
.delivery .head{position:absolute;left:478px;top:12px;font-size:25px;font-weight:700}
.delivery .price{position:absolute;left:534px;top:46px;font-size:23px;font-weight:700;text-decoration:line-through}
.delivery .call{position:absolute;left:930px;top:23px;width:162px;height:44px;background:var(--white);color:var(--red);display:flex;align-items:center;justify-content:center;gap:8px;font-size:14px;font-weight:600}

.brand-box{position:absolute;top:1848px;width:140px;height:83px;border:1px solid #e6e6e6;display:flex;align-items:center;justify-content:center;font-size:18px;font-weight:600;color:#444}

.contact{position:absolute;left:0;top:1983px;width:1200px;height:564px;background:var(--soft)}
.field{position:absolute;left:114px;width:307px;height:40px;border:1px solid #b9b9b9;background:var(--white);display:flex;align-items:center;gap:8px;padding-left:18px;font-size:14px;color:#777}
.message{position:absolute;left:114px;top:2261px;width:307px;height:209px;border:1px solid #b9b9b9;background:var(--white);padding:14px 16px;font-size:13px;color:#888}
.send{position:absolute;left:114px;top:2485px;width:124px;height:31px;background:var(--red);color:var(--white);font-size:13px;display:flex;align-items:center;justify-content:center}
.col-head{position:absolute;top:2106px;font-size:14px;font-weight:700;padding-bottom:4px;border-bottom:2px solid var(--red)}
.detail{position:absolute;left:473px;display:flex;gap:14px;font-size:13px;line-height:19px;color:#444}
.links{position:absolute;top:2145px;font-size:13px;line-height:20px;color:#555}
.map{position:absolute;left:762px;top:2250px;width:293px;height:220px;background:linear-gradient(135deg,#eceae4,#dfe3e8);border:1px solid #ddd}
.follow{position:absolute;left:470px;top:2372px;font-size:13px}
.follow span{color:var(--blue)}
.follow-icons{position:absolute;left:474px;top:2418px;display:flex;gap:26px}
.follow-icons div{width:14px;height:14px;border-radius:50%;background:#222}
.footer{position:absolute;left:0;top:2547px;width:1200px;height:38px;background:#e4e7ec;font-size:12px;color:#777;display:flex;align-items:center;justify-content:center}
</style>
</head>
<body>

<header class="topbar">
  <div class="item" style="left:98px;border-left:1px solid #e0e0e0"><span class="social-dot"></span></div>
  <div class="item" style="left:130px"><span class="social-dot"></span></div>
  <div class="item" style="left:162px"><span class="social-dot"></span></div>
  <div class="item" style="left:196px">
    <svg width="13" height="13" viewBox="0 0 24 24"><path d="M6.6 10.8a15 15 0 0 0 6.6 6.6l2.2-2.2a1 1 0 0 1 1-.25 11 11 0 0 0 3.6.6 1 1 0 0 1 1 1V20a1 1 0 0 1-1 1A17 17 0 0 1 3 4a1 1 0 0 1 1-1h3.5a1 1 0 0 1 1 1 11 11 0 0 0 .6 3.6 1 1 0 0 1-.25 1z" fill="#888"/></svg>
    1 555 010 4841</div>
  <div class="item" style="left:393px;border-left:1px solid #e0e0e0">
    <svg width="14" height="11" viewBox="0 0 24 18"><rect x="1" y="1" width="22" height="16" fill="#888"/><path d="M1 1l11 9 11-9" stroke="#f3f3f3" stroke-width="2" fill="none"/></svg>
    brightcoralinc@mailbox.example</div>
  <div class="item" style="left:842px;border-left:1px solid #e0e0e0">
    <svg width="14" height="13" viewBox="0 0 24 22"><path d="M12 21 3 12a5 5 0 0 1 9-6 5 5 0 0 1 9 6z" fill="none" stroke="#888" stroke-width="2"/></svg>Wishlist</div>
  <div class="item" style="left:935px">
    <svg width="12" height="14" viewBox="0 0 20 24"><rect x="2" y="10" width="16" height="12" fill="none" stroke="#888" stroke-width="2"/><path d="M5 10V6a5 5 0 0 1 10 0v4" fill="none" stroke="#888" stroke-width="2"/></svg>Register</div>
  <div class="item" style="left:1024px">
    <svg width="14" height="12" viewBox="0 0 24 20"><path d="M10 4 4 10l6 6M4 10h12M14 2h7v16h-7" fill="none" stroke="#888" stroke-width="2"/></svg>Log In</div>
</header>

<nav class="navbar">
  <div class="brand">BRIGHT CORAL INC</div>
  <div class="nav-links">
    <a class="active" href="#">About Us</a>
    <a href="#">Phone Repair</a>
    <a href="#">Bill Payments</a>
    <a href="#">Products</a>
    <a href="#">Contact</a>
    <a href="#" style="padding:0 22px">Shop</a>
    <a href="#" style="padding:0 22px"><svg width="18" height="18" viewBox="0 0 24 24"><circle cx="10" cy="10" r="7" fill="none" stroke="#777" stroke-width="2"/><path d="m15 15 6 6" stroke="#777" stroke-width="2"/></svg></a>
    <a href="#" style="gap:4px;padding:0 22px;border-right:1px solid #eee"><svg width="14" height="16" viewBox="0 0 20 24"><rect x="2" y="7" width="16" height="15" fill="none" stroke="#777" stroke-width="2"/><path d="M6 7V5a4 4 0 0 1 8 0v2" fill="none" stroke="#777" stroke-width="2"/></svg>10</a>
  </div>
</nav>

<section class="hero" role="img" aria-label="Blurred warm café lights behind a wooden table">
  <div class="hero-phones" role="img" aria-label="Two white smartphones standing on the table, one showing the lock screen and one the home screen"></div>
  <div class="hero-copy">
    <div class="lead">We can come</div>
    <h1>To You Fix Your Phone</h1>
    <div class="sub">In your home or your work</div>
    <p>Lorem ipsum dolor sit amet, consectetur adipiscing elit, sed do eiusmod tempor incididunt ut labore et dolore magna aliqua.</p>
    <div class="btn-red">Learn More
      <svg width="15" height="15" viewBox="0 0 24 24"><circle cx="12" cy="12" r="10" fill="none" stroke="#fff" stroke-width="2"/><path d="M8 12h8m-3-3 3 3-3 3" fill="none" stroke="#fff" stroke-width="2"/></svg></div>
  </div>
</section>

<h2 class="section-title" style="top:750px"><span>((</span> Services <span>))</span></h2>

<div class="service" style="left:112px">
  <svg width="36" height="54" viewBox="0 0 36 54"><rect x="2" y="2" width="32" height="50" rx="4" fill="none" stroke="var(--red)" stroke-width="2"/><path d="M2 10h32M2 42h32" stroke="var(--red)" stroke-width="2"/><circle cx="18" cy="47" r="2" fill="var(--red)"/></svg>
  <h3>Sell Phones</h3>
  <p>Lorem ipsum dolor sit amet, consectetur adipiscing elit. Suspendisse viverra mauris eget tortor imperdiet.</p>
</div>
<div class="service" style="left:451px">
  <svg width="36" height="54" viewBox="0 0 36 54"><rect x="2" y="2" width="32" height="50" rx="4" fill="none" stroke="var(--red)" stroke-width="2"/><path d="M2 10h32M2 42h32" stroke="var(--red)" stroke-width="2"/><path d="M10 16l16 18M26 16 10 34" stroke="var(--red)" stroke-width="3"/></svg>
  <h3>Phone Repair</h3>
  <p>Lorem ipsum dolor sit amet, consectetur adipiscing elit. Suspendisse viverra mauris eget tortor imperdiet.</p>
</div>
<div class="service" style="left:790px">
  <svg width="62" height="54" viewBox="0 0 62 54"><path d="M8 2v18a10 10 0 0 0 20 0V8a6 6 0 0 1 12 0v40" fill="none" stroke="var(--red)" stroke-width="2"/><rect x="2" y="2" width="12" height="10" rx="3" fill="none" stroke="var(--red)" stroke-width="2"/><rect x="44" y="14" width="14" height="26" rx="3" fill="none" stroke="var(--red)" stroke-width="2"/></svg>
  <h3>Phone Accessories</h3>
  <p>Lorem ipsum dolor sit amet, consectetur adipiscing elit. Suspendisse viverra mauris eget tortor imperdiet.</p>
</div>

<div class="tabs"><div>Featured</div><div>New Arrivals</div><div class="on">Best Seller</div></div>

<article class="product" style="left:117px">
  <div class="shot" role="img" aria-label="Black smartphone showing home screen"></div>
  <div class="name">Product</div><div class="price">$60.00</div>
  <div class="buy">Buy Now</div>
</article>
<article class="product" style="left:359px">
  <div class="shot" role="img" aria-label="Smartphone showing a clock and weather widget" style="background:linear-gradient(180deg,#7fd3e6,#1f7fa3)"></div>
  <div class="name">Product</div><div class="price">$200.00</div>
  <div class="buy">Buy Now</div>
</article>
<article class="product lift" style="left:608px">
  <div class="shot" role="img" aria-label="Dark grey smartphone showing app icons" style="left:45px;background:linear-gradient(160deg,#5a5f68,#1e2a3a)"></div>
  <div class="tools">
    <div><svg width="16" height="14" viewBox="0 0 24 22"><path d="M12 21 3 12a5 5 0 0 1 9-6 5 5 0 0 1 9 6z" fill="none" stroke="#444" stroke-width="2"/></svg></div>
    <div><svg width="16" height="12" viewBox="0 0 24 16"><path d="M1 8q11-14 22 0-11 14-22 0z" fill="none" stroke="#444" stroke-width="2"/><circle cx="12" cy="8" r="3" fill="#444"/></svg></div>
    <div><svg width="16" height="14" viewBox="0 0 24 20"><path d="M2 6h18l-4-4M22 14H4l4 4" fill="none" stroke="#444" stroke-width="2"/></svg></div>
  </div>
  <div class="name">Product</div><div class="price">$240.00</div>
  <div class="buy on">Buy Now</div>
</article>
<article class="product" style="left:860px">
  <div class="shot" role="img" aria-label="Black smartphone showing a pink flower wallpaper" style="background:radial-gradient(circle at 50% 55%,#c04fa0 0,#2a0f2a 35%,#0b0b0b 60%)"></div>
  <div class="name">Product</div><div class="price">$500.00</div>
  <div class="buy">Buy Now</div>
</article>

<section class="delivery">
  <svg class="abs" style="left:124px;top:0" width="110" height="88" viewBox="0 0 110 88"><g fill="none" stroke="#fff" stroke-width="2.5" opacity=".85"><circle cx="42" cy="16" r="13"/><path d="M42 9v7h6"/><path d="M4 34h58v34H4zM62 44h24l14 14v10H62"/><circle cx="22" cy="72" r="7"/><circle cx="82" cy="72" r="7"/></g></svg>
  <div class="label">Fast Delivery</div>
  <div class="head">We Deliver Harborview</div>
  <div class="price">15$ Only</div>
  <div class="call">CALL NOW
    <svg width="14" height="14" viewBox="0 0 24 24"><circle cx="12" cy="12" r="10" fill="none" stroke="var(--red)" stroke-width="2"/><path d="M8 12h8m-3-3 3 3-3 3" fill="none" stroke="var(--red)" stroke-width="2"/></svg></div>
</section>

<h2 class="section-title" style="top:1776px"><span>((</span> Top Brands <span>))</span></h2>
<div class="brand-box" style="left:114px">Tevo Mobile</div>
<div class="brand-box" style="left:275px">Ultrava</div>
<div class="brand-box" style="left:447px">Nettide</div>
<div class="brand-box" style="left:616px">Sorvanta</div>
<div class="brand-box" style="left:780px">Orchard</div>
<div class="brand-box" style="left:948px">Bluebit</div>

<section class="contact"></section>
<h2 class="section-title" style="top:2026px"><span>((</span> Get in touch <span>))</span></h2>

<div class="field" style="top:2103px"><svg width="14" height="14" viewBox="0 0 24 24"><circle cx="12" cy="8" r="5" fill="none" stroke="#888" stroke-width="2"/><path d="M3 22a9 9 0 0 1 18 0" fill="none" stroke="#888" stroke-width="2"/></svg>Name</div>
<div class="field" style="top:2155px"><svg width="14" height="12" viewBox="0 0 24 18"><rect x="1" y="1" width="22" height="16" fill="none" stroke="#888" stroke-width="2"/><path d="M1 1l11 9 11-9" stroke="#888" stroke-width="2" fill="none"/></svg>Email address</div>
<div class="field" style="top:2207px"><svg width="14" height="14" viewBox="0 0 24 24"><path d="M3 21h18M5 17l11-11 3 3-11 11H5z" fill="none" stroke="#888" stroke-width="2"/></svg>Subject</div>
<div class="message">Type your message here...</div>
<div class="send">Send Message</div>

<div class="col-head" style="left:473px">Contact Details</div>
<div class="detail" style="top:2145px"><svg width="12" height="16" viewBox="0 0 18 24"><path d="M9 23S2 14 2 9a7 7 0 0 1 14 0c0 5-7 14-7 14z" fill="none" stroke="var(--blue)" stroke-width="2"/><circle cx="9" cy="9" r="2.5" fill="var(--blue)"/></svg><span>48 Harbor Lane FAIRVIEW, NY<br>10900.</span></div>
<div class="detail" style="top:2201px"><svg width="12" height="16" viewBox="0 0 16 24"><rect x="1" y="1" width="14" height="22" rx="2" fill="none" stroke="var(--blue)" stroke-width="2"/></svg><span>1 555 010 4841</span></div>
<div class="detail" style="top:2234px"><svg width="14" height="14" viewBox="0 0 24 24"><path d="M6.6 10.8a15 15 0 0 0 6.6 6.6l2.2-2.2a1 1 0 0 1 1-.25 11 11 0 0 0 3.6.6 1 1 0 0 1 1 1V20a1 1 0 0 1-1 1A17 17 0 0 1 3 4a1 1 0 0 1 1-1h3.5a1 1 0 0 1 1 1 11 11 0 0 0 .6 3.6 1 1 0 0 1-.25 1z" fill="none" stroke="var(--blue)" stroke-width="2"/></svg><span>1 555 010 4841</span></div>
<div class="detail" style="top:2270px"><svg width="14" height="14" viewBox="0 0 24 24"><rect x="2" y="6" width="20" height="13" fill="none" stroke="var(--blue)" stroke-width="2"/><path d="m2 6 10 8 10-8" fill="none" stroke="var(--blue)" stroke-width="2"/></svg><span>BRIGHTCORALINC@MAILBOX.EXAMPLE</span></div>
<div class="detail" style="top:2300px"><svg width="14" height="14" viewBox="0 0 24 24"><rect x="2" y="6" width="20" height="13" fill="none" stroke="var(--blue)" stroke-width="2"/><path d="m2 6 10 8 10-8" fill="none" stroke="var(--blue)" stroke-width="2"/></svg><span>BRIGHTCORALINC@MAILBOX.EXAMPLE</span></div>
<div class="follow">Follow us <span>@Bright-Coral Inc.</span></div>
<div class="follow-icons"><div></div><div></div><div></div><div></div><div></div></div>

<div class="col-head" style="left:758px">Quick Links</div>
<div class="links" style="left:758px">Login<br>New Customers<br>Products<br>Phone Repair</div>
<div class="col-head" style="left:926px">Customer Service</div>
<div class="links" style="left:926px">Contact Us<br>Privacy Policy<br>Terms &amp;<br>Conditions</div>
<div class="map" role="img" aria-label="Street map showing the store location"></div>

<footer class="footer">© Copyright 2017 Bright-Coral Inc | All right reseverd</footer>

</body>
</html>
```